Business Card

Need business cards and small flyers for a musical band

Target Market(s)

Promoters, clients seeking to hire a Latin band

Industry/Entity Type

Business

Requirements
Must have
• The name of the band is Orchestra Brisa so want to have the background with a fire design, with black card and the name of the band in RED, maybe a combination of Red with some yellow. See attached idea.
Nice to have
• See attached files for some ideas.

```html
<!DOCTYPE html>
<html lang="en">
<head>
<meta charset="utf-8">
<title>Orchestra Brisa – Business Card</title>
<link rel="stylesheet" href="https://fonts.googleapis.com/css2?family=Cormorant+Garamond:ital,wght@0,700;1,500&display=swap">
<style>
  :root {
    --page-bg: #cfcfcc;
    --card-black: #050403;
    --fire-deep: #3a0c02;
    --fire-red: #a52a05;
    --fire-orange: #e0700f;
    --fire-yellow: #f4b43a;
    --band-name: #f29a2a;
    --gold-line: #e8a623;
    --text-white: #ffffff;
  }
  * { margin: 0; padding: 0; box-sizing: border-box; }
  html, body {
    width: 1200px;
    height: 900px;
    overflow: hidden;
    background: var(--page-bg);
  }
  .business-card {
    position: absolute;
    left: 90px;
    top: 150px;
    width: 1020px;
    height: 600px;
    background: var(--card-black);
    box-shadow: 0 14px 30px rgba(0,0,0,0.35);
  }
  .fire-background {
    position: absolute;
    inset: 24px;
    background:
      radial-gradient(ellipse 40% 35% at 30% 30%, rgba(244,180,58,0.55), transparent 70%),
      radial-gradient(ellipse 35% 40% at 75% 55%, rgba(224,112,15,0.7), transparent 70%),
      radial-gradient(ellipse 50% 30% at 55% 80%, rgba(165,42,5,0.8), transparent 75%),
      linear-gradient(160deg, var(--fire-red) 0%, var(--fire-orange) 40%, var(--fire-red) 70%, var(--fire-deep) 100%);
  }
  .band-name {
    position: absolute;
    left: 0;
    right: 0;
    top: 90px;
    text-align: center;
    font-family: "Cormorant Garamond", serif;
    font-weight: 700;
    color: var(--band-name);
    line-height: 0.9;
  }
  .band-name__first {
    display: block;
    font-size: 100px;
    padding-left: 250px;
    letter-spacing: 2px;
  }
  .band-name__second {
    display: block;
    font-size: 210px;
    letter-spacing: 14px;
    margin-top: -20px;
  }
  .contact-panel {
    position: absolute;
    left: 0;
    top: 430px;
    width: 600px;
    height: 150px;
  }
  .contact-panel svg {
    position: absolute;
    inset: 0;
  }
  .contact-details {
    position: absolute;
    left: 50px;
    top: 10px;
    font-family: "Cormorant Garamond", serif;
    font-style: italic;
    font-weight: 500;
    font-size: 44px;
    line-height: 46px;
    letter-spacing: 2px;
    color: var(--text-white);
    list-style: none;
  }
</style>
</head>
<body>
  <article class="business-card">
    <div class="fire-background" role="img" aria-label="Background of swirling orange and yellow flames"></div>

    <h1 class="band-name">
      <span class="band-name__first">Orchestra</span>
      <span class="band-name__second">BRISA</span>
    </h1>

    <div class="contact-panel">
      <svg width="600" height="150" viewBox="0 0 600 150" aria-hidden="true">
        <polygon points="0,2 590,2 535,148 0,148" fill="#050403"/>
        <polyline points="0,2 590,2 535,148 0,148" fill="none" stroke="#e8a623" stroke-width="3"/>
      </svg>
      <ul class="contact-details">
        <li class="contact-name">Rafael Montoya</li>
        <li class="contact-role">Musical Director</li>
        <li class="contact-phone">813-555-0172</li>
      </ul>
    </div>
  </article>
</body>
</html>
```